Square Business Cards for Our Restaurant / Event Venue

We need square business cards designed for the management team of our event venue and restaurant. On one side of the card should be the the Lantern Hall 7 logo and URL www.lanternhall7.example. On the other side should be the Ember Logo and URL www.emberonfive.example. All employee details should be on the side with Ember logo. There will be a total of 5 cards to be created with the design.

Corinne Baldrath
corinne@lanternhall7.example

main 202.555.4817
direct 202.555.0392

3418 Westbury Lane NW
Washington, DC 20019

```html
<!DOCTYPE html>
<html lang="en">
<head>
<meta charset="utf-8">
<title>Lantern Hall 7 – Square Business Card</title>
<link href="https://fonts.googleapis.com/css2?family=Montserrat:wght@400;500;600&display=swap" rel="stylesheet">
<style>
  :root {
    --stage: #9a9a9a;
    --card: #fafafa;
    --brand-red: #9e2824;
    --ink: #1a1a1a;
    --white: #ffffff;
  }
  * { margin: 0; padding: 0; box-sizing: border-box; }
  html, body { width: 1200px; height: 759px; overflow: hidden; }
  body {
    background: var(--stage);
    position: relative;
    font-family: "Montserrat", sans-serif;
    color: var(--ink);
  }
  .card {
    position: absolute;
    top: 194px;
    width: 370px;
    height: 370px;
    background: var(--card);
    overflow: hidden;
  }
  .card--front { left: 188px; }
  .card--back { left: 641px; }

  .brand-disc {
    position: absolute;
    left: 73px; top: 51px;
    width: 224px; height: 224px;
    border-radius: 50%;
    background: var(--brand-red);
    display: flex; align-items: center; justify-content: center;
    text-align: center;
  }
  .brand-disc__name {
    color: var(--white);
    font-weight: 500;
    font-size: 30px;
    line-height: 1.15;
  }
  .front-url {
    position: absolute;
    left: 0; right: 0; top: 331px;
    text-align: center;
    font-size: 14.5px;
  }
  .accent { color: var(--brand-red); }

  .venue-name {
    position: absolute;
    left: 22px; top: 58px;
    font-size: 62px;
    font-weight: 600;
    color: var(--ink);
    letter-spacing: -1px;
  }
  .contact-list {
    position: absolute;
    left: 21px; top: 176px;
    list-style: none;
    font-size: 15.5px;
    line-height: 19.5px;
  }
  .contact-list li { display: flex; align-items: center; gap: 8px; white-space: nowrap; }
  .contact-list svg { width: 13px; height: 13px; fill: var(--brand-red); flex: none; }
  .contact-list .inline-icon { margin-left: 4px; margin-right: -4px; }
  .address {
    position: absolute;
    left: 21px; top: 250px;
    font-size: 15.5px;
    line-height: 19.5px;
    font-style: normal;
  }
  .wave { position: absolute; left: 0; top: 0; width: 370px; height: 370px; }
  .person-name {
    position: absolute;
    right: 34px; top: 308px;
    text-align: right;
    color: var(--white);
    font-size: 22px;
    font-weight: 600;
    line-height: 23px;
  }
</style>
</head>
<body>

<section class="card card--front">
  <div class="brand-disc">
    <span class="brand-disc__name">Lantern<br>Hall 7</span>
  </div>
  <p class="front-url">www.<span class="accent">lanternhall7</span>.example</p>
</section>

<section class="card card--back">
  <div class="venue-name">Ember</div>

  <ul class="contact-list">
    <li>
      <svg viewBox="0 0 16 16"><path d="M8 1a7 7 0 1 0 0 14A7 7 0 0 0 8 1zm5.9 6.3h-2.6a11 11 0 0 0-.8-4.2 6 6 0 0 1 3.4 4.2zM8 2.2c.8 1 1.5 2.8 1.6 5.1H6.4C6.5 5 7.2 3.2 8 2.2zM5.5 3.1a11 11 0 0 0-.8 4.2H2.1a6 6 0 0 1 3.4-4.2zM2.1 8.7h2.6a11 11 0 0 0 .8 4.2 6 6 0 0 1-3.4-4.2zM8 13.8c-.8-1-1.5-2.8-1.6-5.1h3.2c-.1 2.3-.8 4.1-1.6 5.1zm2.5-.9a11 11 0 0 0 .8-4.2h2.6a6 6 0 0 1-3.4 4.2z"/></svg>
      <span>www.<span class="accent">emberonfive</span>.example</span>
    </li>
    <li>
      <svg viewBox="0 0 16 16"><path d="M4.2 1.5l2 2.6c.3.4.2.9-.1 1.2l-1 1c.8 1.6 2 2.9 3.6 3.7l1-1c.3-.3.8-.4 1.2-.1l2.6 2c.4.3.5.9.1 1.3l-1.3 1.4c-.5.5-1.2.7-1.9.5C6.2 13 3 9.8 1.9 5.6c-.2-.7 0-1.4.5-1.9L3 1.4c.4-.4.9-.3 1.2.1z"/></svg>
      <span>202.555.4817</span>
      <svg class="inline-icon" viewBox="0 0 16 16"><path d="M1 5c0-1.5 3-2.5 7-2.5S15 3.5 15 5v1.3h-3.2V4.9c-1-.3-2.4-.4-3.8-.4s-2.8.1-3.8.4v1.4H1zm3 2h8l2 6.5H2zm4 1.3a2 2 0 1 0 0 4 2 2 0 0 0 0-4z"/></svg>
      <span>202.555.0392</span>
    </li>
    <li>
      <svg viewBox="0 0 16 16"><path d="M1 3h14v10H1zm1.5 1.4v.3L8 8.8l5.5-4.1v-.3zm0 2.1v5.1l3.4-2.6zm11 0l-3.4 2.5 3.4 2.6zM7.1 9.9l-1-.7-3.3 2.4h10.4l-3.3-2.4-1 .7a1.5 1.5 0 0 1-1.8 0z"/></svg>
      <span>corinne@<span class="accent">lanternhall7</span>.example</span>
    </li>
  </ul>

  <address class="address">3418 Westbury Lane<br>NW Washington,<br>DC 20019</address>

  <svg class="wave" viewBox="0 0 370 370" aria-hidden="true">
    <path d="M0 340 C40 366 120 370 190 334 C250 302 300 290 370 288 L370 370 L0 370 Z" fill="var(--brand-red)"/>
    <path d="M0 312 C70 352 140 350 200 316 C255 284 310 272 370 272 L370 280 C310 280 258 292 204 322 C140 358 60 360 0 326 Z" fill="var(--ink)"/>
    <path d="M18 340 C80 360 140 356 190 330" fill="none" stroke="var(--ink)" stroke-width="1.5"/>
  </svg>

  <div class="person-name">Corinne<br>Baldrath</div>
</section>

</body>
</html>
```